Stationary Design For New Dynamic Company

Hi there we require stationary designed for our new company, we have used "Pixel Harbor" recently for our logo and were very impressed with all of the designers that contributed towards the final result.
What we require now is the following:
Letter head layout (A4)
Business Cards (5 people)
With Compliments slips
Envelopes
Email stationary
We would like to use our current logo design and I have included it for your use (JPEG is the one we have chosen and I have attached an EPS file for your use). Our company specializes in architectural cladding and our products are used by architects, builders and private clients, so we wish for the stationary to be suitable and attractive to our clientele.
I thank everyone in advance for your contributions.
Thank you to all that have provided your designs for this project, I apologize for not providing feedback as I have been away. I have looked at everyone's designs and they all look great and I will come back to those designers that I wish to have changes made sometime today.
Once again a big thank you to all involved.
Business

```html
<!DOCTYPE html>
<html lang="en">
<head>
<meta charset="utf-8">
<title>Steelvane Stationery</title>
<link href="https://fonts.googleapis.com/css2?family=Didact+Gothic&family=Montserrat:wght@700&display=swap" rel="stylesheet">
<style>
  :root {
    --navy: #1f3f7f;
    --orange: #f08a1c;
    --ink: #2b2b2b;
    --muted: #555;
    --paper: #ffffff;
    --bg: #ffffff;
    --shadow: rgba(0,0,0,0.28);
  }
  html, body { margin: 0; padding: 0; overflow: hidden; }
  body {
    width: 849px; height: 1200px; position: relative;
    background: var(--bg);
    font-family: "Didact Gothic", "Century Gothic", sans-serif;
    color: var(--ink);
  }
  .sheet {
    position: absolute; background: var(--paper);
    box-shadow: 1px 2px 5px var(--shadow);
    border: 1px solid #e4e4e4;
    box-sizing: border-box;
  }
  .brand {
    display: flex; align-items: center; gap: 5px;
    color: var(--navy); font-weight: 400; letter-spacing: 0.5px;
  }
  .brand-square { background: var(--orange); flex: none; }
  .edge-bar { position: absolute; background: var(--navy); }
  .contact { margin: 0; line-height: 1.25; letter-spacing: 2px; }

  /* business card */
  .business-card { left: 40px; top: 40px; width: 104px; height: 360px; }
  .business-card .person { position: absolute; left: 10px; top: 11px; }
  .business-card .name { font-family: "Montserrat", sans-serif; font-weight: 700; font-size: 10px; letter-spacing: 0.4px; margin: 0; }
  .business-card .role { font-size: 6px; margin: 1px 0 0; }
  .business-card .edge-bar { left: 0; top: 215px; width: 6px; height: 50px; }
  .business-card .brand { position: absolute; left: 10px; top: 233px; font-size: 13px; }
  .business-card .brand-square { width: 9px; height: 9px; }
  .business-card .contact { position: absolute; left: 10px; top: 272px; font-size: 7px; letter-spacing: 1.6px; }

  /* letterhead */
  .letterhead { left: 390px; top: 40px; width: 410px; height: 578px; }
  .letterhead .edge-bar { left: 321px; top: 20px; width: 3px; height: 24px; }
  .letterhead .brand { position: absolute; left: 328px; top: 25px; font-size: 12px; }
  .letterhead .brand-square { width: 7px; height: 7px; }
  .letterhead .contact { position: absolute; left: 328px; top: 48px; font-size: 5px; letter-spacing: 1.4px; color: var(--muted); }

  /* compliments slip */
  .compliments { left: 161px; top: 585px; width: 646px; height: 282px; }
  .compliments .edge-bar { left: 12px; top: 26px; width: 4px; height: 28px; }
  .compliments .brand { position: absolute; left: 20px; top: 30px; font-size: 14px; }
  .compliments .brand-square { width: 8px; height: 8px; }
  .compliments .message { position: absolute; left: 20px; top: 56px; font-size: 6px; margin: 0; }
  .compliments .contact { position: absolute; right: 40px; top: 68px; font-size: 6px; letter-spacing: 0.5px; color: var(--muted); }
  .compliments .slip-title { position: absolute; left: 20px; top: 228px; margin: 0; font-family: "Montserrat", sans-serif; font-weight: 700; font-size: 24px; letter-spacing: 0.3px; }

  /* envelope */
  .envelope { left: 40px; top: 850px; width: 653px; height: 322px; }
  .envelope .edge-bar { left: 0; top: 204px; width: 5px; height: 30px; }
  .envelope .brand { position: absolute; left: 12px; top: 210px; font-size: 14px; }
  .envelope .brand-square { width: 8px; height: 8px; }
  .envelope .contact { position: absolute; left: 12px; top: 237px; font-size: 6.5px; letter-spacing: 1.6px; }
</style>
</head>
<body>
  <section class="sheet business-card" aria-label="Business card">
    <div class="person">
      <p class="name">YOUR NAME</p>
      <p class="role">Your Position</p>
    </div>
    <div class="edge-bar"></div>
    <div class="brand"><span class="brand-square"></span>STEELVANE</div>
    <p class="contact">YourHouse<br>YourStreet<br>CountryPostcode<br>Tel:01232456789<br>Fax:01232456789<br>your@youremail.com<br>www.yourweb.com</p>
  </section>

  <section class="sheet letterhead" aria-label="Letterhead">
    <div class="edge-bar"></div>
    <div class="brand"><span class="brand-square"></span>STEELVANE</div>
    <p class="contact">YourHouse<br>YourStreet<br>CountryPostcode<br>Tel:01232456789<br>Fax:01232456789<br>your@youremail.com<br>www.yourweb.com</p>
  </section>

  <section class="sheet envelope" aria-label="Envelope">
    <div class="edge-bar"></div>
    <div class="brand"><span class="brand-square"></span>STEELVANE</div>
    <p class="contact">YourHouse<br>YourStreet<br>CountryPostcode<br>Tel:01232456789<br>Fax:01232456789<br>your@youremail.com<br>www.yourweb.com</p>
  </section>

  <section class="sheet compliments" aria-label="With compliments slip">
    <div class="edge-bar"></div>
    <div class="brand"><span class="brand-square"></span>STEELVANE</div>
    <p class="message">Company Message</p>
    <p class="contact">Your House<br>Your Street<br>Town<br>Country Postcode<br>T: 0123 2456 789<br>M: 0123 2456 789<br>F: 0123 2456 789<br>you@youremail.com<br>www.yourweb.com</p>
    <h1 class="slip-title">With Compliments</h1>
  </section>
</body>
</html>
```